Retail korea clothing store needs a logo desgin

Retail clothing store. Our main customer is 28-35 years women. our store is located at japan town San Francisco. our theme color are black , White and sliver color. we would like modern.

Clothing

```html
<!DOCTYPE html>
<html lang="en">
<head>
<meta charset="utf-8">
<title>NURI — Business Card</title>
<link rel="stylesheet" href="https://fonts.googleapis.com/css2?family=Raleway:ital,wght@0,200;1,200;1,300&display=swap">
<style>
  :root {
    --ink: #000000;
    --paper: #ffffff;
    --charcoal: #333333;
    --taupe: #6f6a6a;
    --pearl: #e9e9e9;
    --label: #f4f4f4;
    --tagline: #8a8a8a;
    --tagline-dark: #4a4a4a;
  }
  html, body {
    margin: 0;
    padding: 0;
    width: 1200px;
    height: 1200px;
    overflow: hidden;
    background: var(--paper);
  }
  .sheet { display: block; width: 1200px; height: 1200px; }
  .brand { font-family: "Raleway", sans-serif; font-weight: 200; font-size: 92px; letter-spacing: -2px; }
  .brand--light { fill: var(--paper); }
  .brand--dark { fill: var(--ink); }
  .tagline { font-family: "Raleway", sans-serif; font-style: italic; font-weight: 300; font-size: 38px; letter-spacing: -1.5px; }
  .tagline--front { fill: var(--tagline); }
  .tagline--back { fill: var(--tagline-dark); }
  .field-label { font-family: "Raleway", sans-serif; font-style: italic; font-weight: 300; font-size: 36px; letter-spacing: -1.5px; fill: var(--label); }
  .field-label--web { fill: var(--tagline-dark); font-size: 30px; }
  .card-base { fill: var(--ink); }
  .card-stripe { fill: var(--charcoal); }
  .layer-taupe { fill: var(--taupe); }
  .layer-pearl { fill: var(--pearl); }
  .layer-silver { fill: url(#silverSheen); }
  .info-panel { fill: url(#panelShade); }
</style>
</head>
<body>
<svg class="sheet" viewBox="0 0 1410 1410" width="1200" height="1200" xmlns="http://www.w3.org/2000/svg" role="img" aria-label="NURI business card, front and back">
  <defs>
    <linearGradient id="silverSheen" x1="0" y1="1" x2="1" y2="0">
      <stop offset="0" stop-color="#4e4e4e"/>
      <stop offset="0.5" stop-color="#9a9a9a"/>
      <stop offset="1" stop-color="#cfcfcf"/>
    </linearGradient>
    <linearGradient id="panelShade" x1="0" y1="1" x2="1" y2="0">
      <stop offset="0" stop-color="#565656"/>
      <stop offset="0.55" stop-color="#6e6e6e"/>
      <stop offset="1" stop-color="#8f8f8f"/>
    </linearGradient>
  </defs>

  <!-- Front of card -->
  <g class="card-front">
    <path class="card-base" d="M80 32 H1166 V510 Q1166 668 1008 668 H80 Z"/>
    <path class="card-stripe" d="M1046 32 H1148 V505 Q1148 618 1046 648 Z"/>
    <text class="brand brand--light" x="624" y="348" text-anchor="middle">NURI</text>
    <text class="tagline tagline--front" x="630" y="468" text-anchor="middle">Korean Clothing.</text>
  </g>

  <!-- Back of card -->
  <g class="card-back">
    <path class="card-base" d="M83 735 H1168 V1220 Q1168 1373 1015 1373 H83 Z"/>
    <path class="layer-taupe" d="M1168 738 C900 758 420 772 210 800 C130 815 112 900 104 1000 L85 1373 H1015 Q1168 1373 1168 1220 Z"/>
    <path class="layer-pearl" d="M1168 744 C820 768 430 790 330 805 C200 828 140 875 128 1000 L90 1373 H1015 Q1168 1373 1168 1220 Z"/>
    <path class="layer-silver" d="M1168 746 C820 770 470 790 352 806 C225 830 165 880 152 1000 L100 1373 H1015 Q1168 1373 1168 1220 Z"/>
    <text class="brand brand--dark" x="1122" y="877" text-anchor="end">NURI</text>
    <path class="info-panel" d="M1152 880 H245 Q175 880 165 960 L115 1360 H1010 Q1152 1360 1152 1215 Z"/>

    <text class="field-label" x="232" y="952">Phone:</text>
    <text class="field-label" x="697" y="952">Fax:</text>
    <text class="field-label" x="232" y="1052">Mobile:</text>
    <text class="field-label" x="700" y="1052">Email:</text>
    <text class="field-label" x="232" y="1152">Address:</text>
    <text class="field-label field-label--web" x="135" y="1345">Website:</text>
    <text class="tagline tagline--back" x="1040" y="1345" text-anchor="end">Korean Clothing.</text>
  </g>
</svg>
</body>
</html>
```